Now Leasing Banner

Looking for a banner that says the following information approx 4' x 30'

Now Leasing Maplewood Terrace 925-318-6054

Target Market(s)

Drive by traffic

Industry/Entity Type

Residential property management

Requirements
Must have
• Clear and readable from a distance

```html
<!DOCTYPE html>
<html lang="en">
<head>
<meta charset="utf-8">
<title>Now Leasing Banner – Maplewood Terrace</title>
<link href="https://fonts.googleapis.com/css2?family=Open+Sans:wght@700;800&display=swap" rel="stylesheet">
<style>
  :root {
    --page: #cfcfcf;
    --banner: #f4f4f4;
    --ink: #1f2322;
    --box: #0d0d0d;
    --reverse: #f2f2f2;
    --sketch-a: #e8e8e8;
    --sketch-b: #dcdcdc;
  }
  * { margin: 0; padding: 0; box-sizing: border-box; }
  html, body { width: 1200px; height: 800px; overflow: hidden; }
  body {
    background: var(--page);
    display: flex;
    align-items: center;
    justify-content: center;
    font-family: "Open Sans", Arial, sans-serif;
  }
  .banner {
    position: relative;
    width: 1160px;
    height: 200px;
    background: var(--banner);
    overflow: hidden;
    box-shadow: 0 2px 10px rgba(0,0,0,0.15);
  }
  .skyline-art {
    position: absolute;
    left: 0; right: 0; bottom: 0;
    height: 150px;
    background: linear-gradient(180deg, var(--banner) 0%, var(--sketch-a) 55%, var(--sketch-b) 100%);
    opacity: 0.7;
  }
  .content {
    position: relative;
    display: grid;
    grid-template-columns: 660px 1fr;
    grid-template-rows: 88px 88px;
    column-gap: 36px;
    row-gap: 0;
    padding: 12px 16px 12px 14px;
    height: 100%;
    align-items: center;
  }
  .headline,
  .call-label {
    font-weight: 800;
    font-size: 76px;
    line-height: 1;
    color: var(--ink);
    text-transform: uppercase;
    white-space: nowrap;
    align-self: start;
  }
  .call-label { text-transform: none; }
  .property-box {
    height: 88px;
    background: var(--box);
    display: flex;
    align-items: center;
    justify-content: center;
    padding: 0 18px;
  }
  .property-name {
    font-weight: 800;
    font-size: 54px;
    line-height: 1;
    color: var(--reverse);
    text-transform: uppercase;
    white-space: nowrap;
  }
  .phone {
    font-weight: 800;
    font-size: 58px;
    line-height: 1;
    color: var(--ink);
    white-space: nowrap;
  }
</style>
</head>
<body>
  <div class="banner">
    <div class="skyline-art" role="img" aria-label="Faint line drawing of a city skyline behind the text"></div>
    <div class="content">
      <div class="headline">Now Leasing</div>
      <div class="call-label">Call</div>
      <div class="property-box"><span class="property-name">Maplewood Terrace</span></div>
      <div class="phone">925-318-6054</div>
    </div>
  </div>
</body>
</html>
```